Sunny Paths and joy Business card

I have a logo, but will like a business card design. Is for a travel agency in Mexico. We focus in family experiences.

I will liek some thing different and unique, from the traditional business card, something to get remmeber for.

Business card information:

Leandro T. Ocampo
leandro@sunnypathsjoy.example

Alameda 482, 3 piso
Col. Tlalpizco
Mexico, D.F. 07320

office: (55) 5000-0142
mobile: (55) 9000-0187

www.sunnypathsjoy.example
@sunnypjoy
blog: sunnypathsandjoy.blogsite.example
facebook: SunnyPathsAndJoy

```html
<!DOCTYPE html>
<html lang="en">
<head>
<meta charset="utf-8">
<title>Sunny Paths and joy — Hang-tag Business Card</title>
<link href="https://fonts.googleapis.com/css2?family=Arimo:wght@400;700&display=swap" rel="stylesheet">
<style>
  :root {
    --page-bg: #ffffff;
    --card-shadow: rgba(0, 0, 0, 0.18);
    --hole: #ffffff;
    --sky-dusk: #a98a9a;
    --sky-orange: #f0a45a;
    --sky-glow: #f7d27a;
    --sky-pale: #f8e7a8;
    --sea-light: #5fd0e6;
    --sea-deep: #2eb3d6;
    --sand: #f2dfb0;
    --back-indigo: #4a5ab0;
    --back-violet: #8b7db4;
    --back-orange: #f3b06d;
    --back-yellow: #f4e6a4;
    --back-white: #fbfbf8;
    --ink: #1b1b1b;
    --brand-blue: #1c4f9f;
    --icon-square: #5f6f8f;
  }

  * { box-sizing: border-box; margin: 0; padding: 0; }

  html, body {
    width: 1200px;
    height: 900px;
    overflow: hidden;
    background: var(--page-bg);
    font-family: "Arimo", Arial, sans-serif;
  }

  .canvas {
    position: relative;
    width: 1200px;
    height: 900px;
  }

  .card {
    position: absolute;
    top: 250px;
    width: 360px;
    height: 560px;
    border-radius: 22px;
    overflow: hidden;
    box-shadow: 0 6px 18px var(--card-shadow);
  }

  .card--front { left: 180px; }
  .card--back  { left: 660px; }

  .punch-hole {
    position: absolute;
    top: 30px;
    left: 50%;
    width: 16px;
    height: 16px;
    margin-left: -8px;
    border-radius: 50%;
    background: var(--hole);
    z-index: 3;
  }

  /* Front */
  .beach-scene {
    position: absolute;
    inset: 0;
    background:
      linear-gradient(172deg, transparent 0 66%, var(--sea-light) 66% 78%, var(--sea-deep) 78% 84%, var(--sand) 84%),
      linear-gradient(180deg, var(--sky-dusk) 0%, var(--sky-orange) 18%, var(--sky-glow) 40%, var(--sky-pale) 62%);
  }

  .brand-name {
    position: absolute;
    left: 0;
    right: 0;
    top: 330px;
    text-align: center;
    font-weight: 700;
    font-size: 40px;
    line-height: 1.05;
    color: var(--brand-blue);
    z-index: 2;
  }

  /* Back */
  .card--back {
    background: linear-gradient(180deg,
      var(--back-indigo) 0%,
      var(--back-violet) 20%,
      var(--back-orange) 42%,
      var(--back-yellow) 62%,
      var(--back-white) 80%);
    color: var(--ink);
  }

  .contact {
    position: absolute;
    left: 100px;
    top: 205px;
  }

  .contact__name {
    font-size: 21px;
    font-weight: 400;
    margin-bottom: 16px;
  }

  .contact__phones,
  .contact__address {
    font-size: 19px;
    line-height: 1.2;
    padding-left: 14px;
  }

  .contact__phones { margin-bottom: 12px; }

  .online {
    position: absolute;
    right: 24px;
    bottom: 36px;
    text-align: right;
    font-size: 14.5px;
    line-height: 1.32;
  }

  .online__line { display: block; }

  .online__mark {
    display: inline-block;
    width: 14px;
    height: 14px;
    margin-right: 6px;
    vertical-align: -2px;
    background: var(--icon-square);
  }
</style>
</head>
<body>
<main class="canvas">

  <section class="card card--front">
    <span class="punch-hole"></span>
    <div class="beach-scene" role="img" aria-label="Illustrated sunset beach scene with palm tree, turquoise sea, sand and a cartoon plane carrying a family"></div>
    <p class="brand-name">Sunny Paths<br>and joy</p>
  </section>

  <section class="card card--back">
    <span class="punch-hole"></span>
    <div class="contact">
      <h1 class="contact__name">Leandro T. Ocampo</h1>
      <p class="contact__phones">w: (55) 5000-0142<br>m: (55) 9000-0187</p>
      <p class="contact__address">Alameda 482, 3 piso<br>Col. Tlalpizco<br>Mexico, D.F. 07320</p>
    </div>
    <p class="online">
      <span class="online__line">leandro@sunnypathsjoy.example</span>
      <span class="online__line">www.sunnypathsjoy.example</span>
      <span class="online__line"><span class="online__mark"></span>sunnypathsandjoy.blogsite.example</span>
      <span class="online__line"><span class="online__mark"></span>SunnyPathsAndJoy</span>
    </p>
  </section>

</main>
</body>
</html>
```